Design of a nice Video On Demand Website

We are looking to design a nice Website for our Video On demand platform we are getting ready to launch. We have put together a file to illustrate the idea and design concept we want. The file also has the menu sections ect. The Designers should look at the file and suggest design ideas based on the concept we put together on the file. The design should be clean yet simple so users can experience a better Navigation. The designer is free to choose whatever color he thinks fit.
Updates

Target Market(s)

Streaming

Number of Pages Required

1 page

Font styles to use
Sans Serif

Colors

Designer to choose colors to be used in the design.

Requirements
Must have
• I will let the designer choose what is best.
Nice to have
• N/A
Should not have
• N/A

```html
<!DOCTYPE html>
<html lang="en">
<head>
<meta charset="utf-8">
<title>VTN – Video On Demand</title>
<link rel="stylesheet" href="https://fonts.googleapis.com/css2?family=Roboto:wght@400;500;700;900&family=Roboto+Condensed:wght@700&display=swap">
<style>
  :root{
    --orange:#f26b21;
    --black:#000;
    --ink:#141414;
    --panel:#1b1b1b;
    --header:rgba(15,15,15,.88);
    --white:#fff;
    --grey:#9a9a9a;
    --light:#d9d9d9;
    --line:#3a3a3a;
    --red:#ff1a1a;
  }
  *{box-sizing:border-box;margin:0;padding:0}
  html,body{width:1200px;height:750px;overflow:hidden;background:var(--ink);font-family:'Roboto',sans-serif;color:var(--white)}
  .page{position:relative;width:1200px;height:750px}

  .hero-photo{position:absolute;left:0;top:0;width:1200px;height:550px;
    background:radial-gradient(ellipse at 70% 40%,#d8cbb4 0%,#a48f6e 35%,#5a4a34 70%,#2c2520 100%);}
  .hero-photo::after{content:"";position:absolute;inset:0;background:linear-gradient(180deg,rgba(0,0,0,.15),rgba(0,0,0,.35))}

  .topbar{position:absolute;left:0;top:0;width:1200px;height:60px;background:var(--header)}
  .menu-toggle{position:absolute;left:69px;top:23px}
  .brand{position:absolute;left:108px;top:14px;display:flex;align-items:center;gap:6px;font-weight:900;font-size:28px;color:var(--orange);letter-spacing:1px}
  .brand .mark{width:12px;height:12px;background:var(--orange)}
  .channels{position:absolute;left:0;top:0;width:0;height:60px;list-style:none}
  .channels li{position:absolute;top:20px;height:20px;line-height:20px;font-weight:900;font-size:15px;color:var(--grey);text-align:center;white-space:nowrap}
  .channels li.active{color:var(--white)}
  .channels li.big{top:14px;height:32px;line-height:32px;font-size:25px;text-align:left}
  .tag{position:absolute;left:461px;top:59px;width:58px;height:20px;background:var(--orange);border-radius:3px;font-weight:500;font-size:12px;text-align:center;line-height:20px}
  .tag::before{content:"";position:absolute;left:25px;top:-5px;border:4px solid transparent;border-bottom-color:var(--orange);border-top:0}
  .search{position:absolute;left:938px;top:13px;width:193px;height:35px;background:#111;border:1px solid #333;display:flex;align-items:center;padding:0 14px;font-size:14px;color:#ddd;justify-content:space-between}

  .sidebar{position:absolute;left:72px;top:60px;width:180px;height:490px;background:var(--panel)}
  .live{position:absolute;left:11px;top:22px;font-weight:700;font-size:17px;letter-spacing:1px}
  .live::after{content:"";position:absolute;left:58px;top:7px;width:9px;height:9px;border-radius:50%;background:var(--red)}
  .nav{position:absolute;left:0;top:74px;width:180px;list-style:none;border-top:1px solid var(--line)}
  .nav li{height:32.3px;display:flex;align-items:center;justify-content:space-between;padding:0 11px 0 12px;font-size:12.5px;border-bottom:1px solid var(--line)}
  .nav li.current{background:var(--light);color:#222}
  .nav svg{width:9px;height:11px}
  .side-brand{position:absolute;left:11px;top:432px;display:flex;align-items:center;gap:5px;font-weight:900;font-size:26px;color:var(--orange)}
  .side-brand .mark{width:11px;height:11px;background:var(--orange)}

  .feature{position:absolute;left:297px;top:215px;width:493px;height:250px;background:rgba(60,60,60,.62)}
  .feature h1{position:absolute;left:33px;top:20px;font-family:'Roboto Condensed',sans-serif;font-weight:700;font-size:37px;color:var(--orange);letter-spacing:.5px}
  .feature .credit{position:absolute;left:34px;top:86px;font-size:17px;white-space:nowrap}
  .feature .note{position:absolute;left:33px;top:126px;font-size:14.5px;white-space:nowrap}
  .watch{position:absolute;left:33px;top:179px;width:159px;height:41px;background:var(--orange);border-radius:3px;display:flex;align-items:center;padding-left:11px;gap:6px;font-weight:700;font-size:14px;letter-spacing:.5px}

  .slider{position:absolute;left:1128px;top:223px;display:flex;flex-direction:column;gap:11px}
  .slider span{width:3px;height:12px;background:#eee;border-radius:2px}
  .slider span.on{background:var(--orange)}

  .legal{position:absolute;left:0;top:550px;width:1200px;height:45px;background:var(--black);display:flex;justify-content:center;align-items:center;font-size:9px;letter-spacing:.6px;color:#ddd;gap:14px}
  .footer-brand{position:absolute;left:560px;top:612px;display:flex;align-items:center;gap:6px;font-weight:900;font-size:30px;color:var(--orange)}
  .footer-brand .mark{width:12px;height:12px;background:var(--orange)}
  .social{position:absolute;left:540px;top:686px;display:flex;gap:12px}
  .social span{width:16px;height:16px;border-radius:50%;background:#888}
  .copyright{position:absolute;left:0;top:726px;width:1200px;text-align:center;font-size:9px;letter-spacing:.5px;color:#ddd}
</style>
</head>
<body>
<div class="page">
  <div class="hero-photo" role="img" aria-label="Three chefs in white caps and aprons plating desserts in an ornate kitchen"></div>

  <header class="topbar">
    <svg class="menu-toggle" width="17" height="13" viewBox="0 0 17 13"><rect x="0" y="0" width="16" height="2" rx="1" fill="#fff"/><rect x="0" y="5.5" width="12" height="2" rx="1" fill="#fff"/><rect x="0" y="11" width="8" height="2" rx="1" fill="#fff"/></svg>
    <div class="brand"><span class="mark"></span>VTN</div>
    <ul class="channels">
      <li style="left:255px;width:55px">VTN 1</li>
      <li style="left:325px;width:55px">VTN 2</li>
      <li style="left:394px;width:54px">VTN 3</li>
      <li class="active" style="left:455px;width:70px">VTN Kids</li>
      <li style="left:528px;width:72px">Radio VTN</li>
      <li style="left:613px;width:72px">Onde 2</li>
      <li style="left:694px;width:70px">Radio Vue</li>
      <li class="big" style="left:773px;width:110px">VTN.info</li>
    </ul>
    <div class="search">Search here...
      <svg width="15" height="15" viewBox="0 0 15 15"><circle cx="6" cy="6" r="5" fill="none" stroke="#fff" stroke-width="1.5"/><line x1="9.7" y1="9.7" x2="14" y2="14" stroke="#fff" stroke-width="1.5"/></svg>
    </div>
  </header>
  <div class="tag">VIDEO</div>

  <aside class="sidebar">
    <div class="live">LIVE</div>
    <ul class="nav">
      <li>My Account<svg viewBox="0 0 9 11"><path d="M1 1l4 4.5L1 10M4 1l4 4.5L4 10" fill="none" stroke="currentColor" stroke-width=".8"/></svg></li>
      <li class="current">Grill des Programmes<svg viewBox="0 0 9 11"><path d="M1 1l4 4.5L1 10M4 1l4 4.5L4 10" fill="none" stroke="currentColor" stroke-width=".8"/></svg></li>
      <li>My Selection<svg viewBox="0 0 9 11"><path d="M1 1l4 4.5L1 10M4 1l4 4.5L4 10" fill="none" stroke="currentColor" stroke-width=".8"/></svg></li>
      <li>Entertainment<svg viewBox="0 0 9 11"><path d="M1 1l4 4.5L1 10M4 1l4 4.5L4 10" fill="none" stroke="currentColor" stroke-width=".8"/></svg></li>
      <li>Series<svg viewBox="0 0 9 11"><path d="M1 1l4 4.5L1 10M4 1l4 4.5L4 10" fill="none" stroke="currentColor" stroke-width=".8"/></svg></li>
      <li>TV Movies<svg viewBox="0 0 9 11"><path d="M1 1l4 4.5L1 10M4 1l4 4.5L4 10" fill="none" stroke="currentColor" stroke-width=".8"/></svg></li>
      <li>Info &amp; Company<svg viewBox="0 0 9 11"><path d="M1 1l4 4.5L1 10M4 1l4 4.5L4 10" fill="none" stroke="currentColor" stroke-width=".8"/></svg></li>
      <li>Sports<svg viewBox="0 0 9 11"><path d="M1 1l4 4.5L1 10M4 1l4 4.5L4 10" fill="none" stroke="currentColor" stroke-width=".8"/></svg></li>
      <li>Humer<svg viewBox="0 0 9 11"><path d="M1 1l4 4.5L1 10M4 1l4 4.5L4 10" fill="none" stroke="currentColor" stroke-width=".8"/></svg></li>
      <li>Youth<svg viewBox="0 0 9 11"><path d="M1 1l4 4.5L1 10M4 1l4 4.5L4 10" fill="none" stroke="currentColor" stroke-width=".8"/></svg></li>
    </ul>
    <div class="side-brand"><span class="mark"></span>VTN</div>
  </aside>

  <section class="feature">
    <h1>THE CHEF</h1>
    <p class="credit">WRITTEN AND DIRECTED BY MARC DELORME</p>
    <p class="note">CANDIDATE ARE SUPPORTED BY PAUL ARNAUD!</p>
    <div class="watch">SEE THE VIDEO
      <svg width="25" height="25" viewBox="0 0 25 25"><circle cx="12.5" cy="12.5" r="12.5" fill="#fff"/><path d="M10 7.5l7 5-7 5z" fill="#f26b21"/></svg>
    </div>
  </section>

  <div class="slider"><span></span><span class="on"></span><span></span><span></span><span></span></div>

  <nav class="legal">
    <span>Mention L`egales</span><span>|</span><span>Conditions G`en`erales D utilisation</span><span>|</span><span>Politique de protection des donnees personnelles</span><span>|</span><span>Cookies</span><span>|</span><span>CGU</span><span>|</span><span>Contacts</span>
  </nav>

  <div class="footer-brand"><span class="mark"></span>VTN</div>
  <div class="social" aria-label="Social links"><span></span><span></span><span></span><span></span><span></span></div>
  <p class="copyright">Copyright © 2019 VTN.COM. All Rights Reserved.</p>
</div>
</body>
</html>
```